Values and Organizational Purpose Signage

We recently solidified our company values, organizatioanal purpose and strategic vision. I'd like to develop some tasteful (not overly corporate) signage of these values to display in our office.

I've attached the hand-written values and purpose that my core team members then initialed acknowleding they align along with the signage at the front of our office to provide some perspective on our brand identity.

Industry/Entity Type

It Company

Font styles to use
Sans Serif

Requirements
Must have
• I'd like to see the values and org purpose depicted as one sign and as separate signs (i.e., values on one sign and org purpose on another). I need it to reflect our brand identity which I've uploaded

```html
<!DOCTYPE html>
<html lang="en">
<head>
<meta charset="utf-8">
<title>Organizational Purpose and Core Values Signage</title>
<link href="https://fonts.googleapis.com/css2?family=Jost:wght@400;500;700&display=swap" rel="stylesheet">
<style>
  :root {
    --ink: #0d3a35;
    --lime: #9bd13a;
    --panel: #ffffff;
    --backdrop: #eef1ec;
    --screw: #123530;
  }
  * { box-sizing: border-box; margin: 0; padding: 0; }
  html, body {
    width: 1200px; height: 748px; overflow: hidden;
    background: var(--backdrop);
    font-family: "Jost", "Futura", sans-serif;
    color: var(--ink);
  }
  .canvas {
    position: relative; width: 1200px; height: 748px;
    display: flex; flex-direction: column; align-items: center;
    justify-content: center; gap: 40px;
  }
  .sign {
    position: relative; width: 480px; background: var(--panel);
    box-shadow: 0 6px 14px rgba(0,0,0,0.18);
    overflow: hidden;
  }
  .screw {
    position: absolute; width: 7px; height: 7px; border-radius: 50%;
    background: var(--screw);
  }
  .screw.tl { top: 8px; left: 6px; }
  .screw.tr { top: 8px; right: 6px; }
  .screw.bl { bottom: 6px; left: 6px; }
  .screw.br { bottom: 6px; right: 6px; }

  /* Purpose sign */
  .sign--purpose { height: 284px; }
  .brand {
    position: absolute; top: 38px; left: 0; right: 0;
    display: flex; align-items: center; justify-content: center; gap: 12px;
    height: 80px;
  }
  .brand-square { width: 22px; height: 22px; background: var(--lime); }
  .brand-name {
    font-size: 38px; font-weight: 700; letter-spacing: 2px; color: var(--ink);
  }
  .purpose-title {
    position: absolute; left: 36px; top: 158px; white-space: nowrap;
    font-size: 27px; font-weight: 700; letter-spacing: 0; line-height: 1;
  }
  .rule { height: 8px; background: var(--lime); }
  .purpose-rule { position: absolute; left: 36px; width: 402px; top: 196px; }
  .purpose-statement {
    position: absolute; left: 41px; top: 210px;
    font-size: 23px; font-weight: 400; line-height: 28px;
  }

  /* Values sign */
  .sign--values { height: 328px; }
  .values-title {
    position: absolute; left: 24px; top: 26px; white-space: nowrap;
    font-size: 35px; font-weight: 700; letter-spacing: 0; line-height: 1;
  }
  .values-list {
    position: absolute; left: 36px; top: 72px; width: 402px; list-style: none;
  }
  .value { display: flex; align-items: center; height: 47px; }
  .value-name {
    width: 170px; font-size: 18px; font-weight: 700; line-height: 20px;
  }
  .value-text {
    flex: 1; font-size: 12.5px; font-weight: 400; line-height: 16.5px;
  }
  .value--last { height: 62px; }
</style>
</head>
<body>
<main class="canvas">

  <section class="sign sign--purpose">
    <span class="screw tl"></span><span class="screw tr"></span>
    <span class="screw bl"></span><span class="screw br"></span>
    <div class="brand">
      <span class="brand-square"></span>
      <span class="brand-name">NORTHVALE</span>
    </div>
    <h1 class="purpose-title">ORGANIZATIONAL PURPOSE</h1>
    <div class="rule purpose-rule"></div>
    <p class="purpose-statement">We deliver simple and digestible<br>solutions to complex matters</p>
  </section>

  <section class="sign sign--values">
    <span class="screw tl"></span><span class="screw tr"></span>
    <span class="screw bl"></span><span class="screw br"></span>
    <h2 class="values-title">CORE VALUES DEFINED</h2>
    <ul class="values-list">
      <li class="value">
        <span class="value-name">RESPECT</span>
        <span class="value-text">We are transparent and receptive to the thoughts, opinion and feelings of others</span>
      </li>
      <li class="rule"></li>
      <li class="value">
        <span class="value-name">INTEGRITY</span>
        <span class="value-text">We uphold our promises</span>
      </li>
      <li class="rule"></li>
      <li class="value">
        <span class="value-name">EXCELLENCE</span>
        <span class="value-text">We continuously strive to be the best in all endeavors</span>
      </li>
      <li class="rule"></li>
      <li class="value value--last">
        <span class="value-name">OPEN<br>MINDEDNESS</span>
        <span class="value-text">We encourage creative and innovative expressions</span>
      </li>
    </ul>
  </section>

</main>
</body>
</html>
```